insurance post card # 2

Please design a postcard in landscape. Conceptually I'd like the card to be funny, and thought provoking. Couple ideas I had for front of the postcard is to display an old, dingy, empty office desk with old empty chair, with typewriter on desk, and an old rotary phone on desk. Somehow make the phone look like its ringing off the hook, with multiple lights lighting up on the phone, or squiggle lines near phone to show commotion, and of course nobody answering it. I'd like text across the top of the image to say something to the effect of "Is Your Insurance Agent Out of the Office Again?
On the back of post card, I'd like it to feel super modern, with high-tech, futuristics image of Detroit. With tag line that read.... "Time to switch to KORBT for better service, better coverage, more choices, and more savings" I've included picture of Detroit to use, pictures of all the companies we represent. highlight our website address. I'd like to keep some white space on the back of the postcard for further customization for our contact information, when we take piece to printing, etc.

```html
<!DOCTYPE html>
<html lang="en">
<head>
<meta charset="utf-8">
<title>KORBT Postcard</title>
<link rel="stylesheet" href="https://fonts.googleapis.com/css2?family=Oswald:wght@500;600&family=Montserrat:wght@400;500;600;800&display=swap">
<style>
  :root {
    --bg: #e4e4e6;
    --teal: #4fa3b5;
    --teal-dark: #2f7f92;
    --navy: #1f3a4d;
    --grey: #6f7479;
    --ink: #2b2f33;
    --white: #ffffff;
    --photo-office-a: #7d7468;
    --photo-office-b: #3d3a36;
    --photo-sky-a: #e9b98e;
    --photo-sky-b: #8fb2c9;
  }
  * { box-sizing: border-box; margin: 0; padding: 0; }
  html, body { width: 876px; height: 1200px; overflow: hidden; }
  body { background: var(--bg); font-family: "Montserrat", sans-serif; position: relative; }

  .card { position: absolute; left: 108px; width: 660px; height: 447px; background: var(--white); overflow: hidden; box-shadow: 0 3px 10px rgba(0,0,0,0.18); }
  .card--front { top: 108px; }
  .card--back { top: 628px; }

  .brand { display: flex; align-items: center; gap: 10px; }
  .brand-mark { width: 22px; height: 22px; background: var(--teal); }
  .brand-name { font-family: "Montserrat", sans-serif; font-weight: 800; font-size: 30px; color: var(--navy); letter-spacing: 1px; }
  .brand-sub { font-size: 10px; font-weight: 500; color: var(--navy); line-height: 1.25; margin-left: 8px; }

  /* Front */
  .front-photo { position: absolute; inset: 0; background: linear-gradient(110deg, var(--photo-office-a), var(--photo-office-b) 70%, #595249); }
  .front-header { position: absolute; left: 0; top: 0; width: 660px; height: 90px; }
  .front-header .brand { position: absolute; left: 168px; top: 18px; }
  .headline { position: absolute; left: 20px; top: 296px; width: 620px; text-align: center; font-family: "Oswald", sans-serif; font-weight: 600; font-size: 37px; line-height: 1.15; color: var(--white); text-transform: uppercase; white-space: nowrap; text-shadow: 0 2px 6px rgba(0,0,0,0.45); }
  .headline .accent { color: var(--teal); }
  .url-band { position: absolute; right: 0; bottom: 0; width: 300px; height: 40px; background: var(--teal); color: var(--white); font-size: 22px; font-weight: 600; display: flex; align-items: center; padding-left: 30px; letter-spacing: 0.5px; }

  /* Back */
  .back-top { position: absolute; left: 0; top: 0; width: 660px; height: 110px; }
  .back-top .brand { position: absolute; left: 24px; top: 24px; }
  .back-photo { position: absolute; left: 0; top: 86px; width: 660px; height: 200px; background: linear-gradient(180deg, var(--photo-sky-b), var(--photo-sky-a) 60%, #6f8ea3); }
  .back-curve { position: absolute; left: 0; top: 280px; }
  .tagline { position: absolute; left: 26px; top: 336px; width: 330px; font-size: 13.5px; font-weight: 600; color: var(--teal-dark); line-height: 1.3; }
  .back-url { position: absolute; left: 26px; top: 405px; font-size: 13px; font-weight: 600; color: var(--teal); }
  .partners { position: absolute; right: 18px; top: 262px; width: 226px; height: 156px; background: var(--white); padding: 12px; display: grid; grid-template-columns: repeat(3, 1fr); gap: 10px 8px; box-shadow: 0 1px 4px rgba(0,0,0,0.15); }
  .partner { background: #cfd8de; border-radius: 2px; }
</style>
</head>
<body>

<section class="card card--front">
  <div class="front-photo" role="img" aria-label="Photo of a group of elderly office workers in suits leaving an office building"></div>
  <svg class="front-header" viewBox="0 0 660 90" aria-hidden="true">
    <path d="M150 0 H660 V62 Q600 74 520 80 L150 88 Z" fill="var(--white)"/>
    <path d="M520 80 Q600 74 660 62 V68 Q600 82 520 86 Z" fill="var(--teal)"/>
  </svg>
  <div class="front-header">
    <div class="brand">
      <span class="brand-mark"></span>
      <span class="brand-name">KORBT</span>
      <span class="brand-sub">Korbt Insurance<br>and Financial Services</span>
    </div>
  </div>
  <h1 class="headline"><span class="accent">Is</span> your insurance agent out of the<br>office again?</h1>
  <div class="url-band">www.korbt.com</div>
</section>

<section class="card card--back">
  <div class="back-photo" role="img" aria-label="Photo of a city skyline at sunset across the river"></div>
  <svg class="back-top" viewBox="0 0 660 110" aria-hidden="true">
    <path d="M0 0 H660 V20 Q420 30 300 96 L0 100 Z" fill="var(--white)"/>
    <path d="M300 96 Q420 30 660 20 V34 Q440 44 330 98 Z" fill="var(--grey)"/>
    <path d="M330 98 Q440 44 660 34 V44 Q460 56 360 100 Z" fill="var(--teal)"/>
  </svg>
  <div class="back-top">
    <div class="brand">
      <span class="brand-mark"></span>
      <span class="brand-name">KORBT</span>
    </div>
  </div>
  <svg class="back-curve" width="660" height="30" viewBox="0 0 660 30" aria-hidden="true">
    <path d="M0 0 Q300 22 660 4 V30 H0 Z" fill="var(--white)"/>
  </svg>
  <p class="tagline">Time to switch to KORBT for better service, better coverage, more choices, and more savings</p>
  <p class="back-url">www.korbt.com</p>
  <div class="partners" aria-label="Partner insurance companies">
    <span class="partner"></span><span class="partner"></span><span class="partner"></span>
    <span class="partner"></span><span class="partner"></span><span class="partner"></span>
    <span class="partner"></span><span class="partner"></span><span class="partner"></span>
    <span class="partner"></span><span class="partner"></span><span class="partner"></span>
  </div>
</section>

</body>
</html>
```